Start up Events company needs a business card design

We are a brand new start up events company that need an impressively designed business card to make the best first impression with our future clients.

Description on company:
- start-up company
- in the events management industry
- selling flagship children related event
- our future clients will mostly be vendors in the alternative education industry. dance schools, music schools, sports camp facilitators, academic establishments
- our target market are kids, parents of kids, mass market

What we need in the business card:
- we currently have a rough design that I have uploaded. we need to brush it up. make it look more professional, more vibrant but keep the meaning of the company which is called "Kite & Lantern"
- a reason for the "Kite & Lantern" concept is because we will be starting off with a flagship event & be branching out into all other related businesses relating to our core highlight which is kids & alternative education.
- this is a tentative logo we have selected - which is a girl on a swing. to represent momentum as a start up company and related to children
- if you have a better logo alternative, please do suggest it to us
- we need more colours, vibrancy yet it has to be sleek and professional.

As we are a start-up company, our budget is tight. If you have a good idea / concept, do take on this project overlooking the tight budget.
If you require any additional information, do feel free to drop us messages!

Thank you designers!

```html
<!DOCTYPE html>
<html lang="en">
<head>
<meta charset="utf-8">
<title>Kite &amp; Lantern — Business Card</title>
<link rel="stylesheet" href="https://fonts.googleapis.com/css2?family=Federo&family=Kotta+One&family=Quicksand:wght@500&display=swap">
<style>
  :root {
    --cream: #f5e0bc;
    --ink: #1e1710;
    --ornament: #3a2c20;
    --yellow: #fbd832;
    --red: #e8574f;
    --crimson: #d0303a;
    --mauve: #b0506e;
    --rose: #c65e7e;
    --lime: #a9d244;
    --olive: #5b8a3a;
    --violet: #8a55a8;
    --divider: #ffffff;
  }
  * { margin: 0; padding: 0; box-sizing: border-box; }
  html, body { width: 1032px; height: 1200px; overflow: hidden; background: var(--divider); }
  .canvas { position: relative; width: 1032px; height: 1200px; }
  .card { position: absolute; left: 0; width: 1032px; background: var(--cream); overflow: hidden; }
  .card--front { top: 0; height: 594px; }
  .card--back { top: 604px; height: 596px; }
  .card__shapes { position: absolute; inset: 0; }
  .brand-title {
    position: absolute; font-family: "Federo", serif; color: var(--ink);
    font-size: 60px; line-height: 1; white-space: nowrap; letter-spacing: 1px;
  }
  .card--front .brand-title { left: 0; width: 1032px; text-align: center; top: 60px; font-size: 58px; }
  .tagline {
    position: absolute; left: 0; width: 1032px; text-align: center; top: 130px;
    font-family: "Quicksand", sans-serif; font-weight: 500; font-size: 31px; color: var(--ink);
  }
  .contact-line {
    position: absolute; left: 548px; font-family: "Quicksand", sans-serif; font-weight: 500;
    font-size: 32px; color: var(--ink); white-space: nowrap; line-height: 1;
  }
  .contact-line--name { top: 258px; }
  .contact-line--phone { top: 352px; }
  .contact-line--email { top: 444px; }
  .logo-mark__name {
    position: absolute; left: 148px; top: 322px; width: 228px; text-align: center;
    font-family: "Federo", serif; font-size: 27px; color: var(--cream); line-height: 1.1;
  }
  .card--back .brand-title { right: 58px; top: 650px; top: 46px; }
  .quote {
    position: absolute; right: 58px; top: 162px; text-align: right;
    font-family: "Kotta One", serif; font-size: 29px; line-height: 48.5px; color: var(--ink);
  }
  .quote__author {
    position: absolute; right: 58px; top: 488px;
    font-family: "Kotta One", serif; font-size: 30px; color: var(--ink); white-space: nowrap;
  }
</style>
</head>
<body>
<main class="canvas">

  <section class="card card--front">
    <svg class="card__shapes" width="1032" height="594" viewBox="0 0 1032 594">
      <path d="M0 0 H104 C118 40 110 92 70 112 C40 122 14 118 0 110 Z" fill="var(--yellow)"/>
      <rect x="49" y="144" width="51" height="39" rx="16" fill="var(--lime)"/>
      <path d="M860 0 H1032 V214 C990 232 920 226 872 196 C842 170 842 90 850 40 Z" fill="var(--red)"/>
      <path d="M952 356 C980 346 1020 348 1032 352 V436 C1010 442 970 442 952 428 C938 410 938 368 952 356 Z" fill="var(--mauve)"/>
      <path d="M412 548 C420 520 470 524 540 526 C600 528 650 530 664 560 L668 594 H402 Z" fill="var(--lime)"/>

      <g class="logo-connectors" stroke="var(--ornament)" stroke-width="3">
        <line x1="370" y1="312" x2="462" y2="283"/>
        <line x1="376" y1="368" x2="462" y2="368"/>
        <line x1="360" y1="412" x2="462" y2="452"/>
        <line x1="128" y1="490" x2="170" y2="450"/>
      </g>

      <circle cx="262" cy="348" r="164" fill="#d9c09b" opacity="0.55" role="img" aria-label="Decorative flourish frame around the logo"/>
      <circle cx="262" cy="348" r="116" fill="var(--mauve)" stroke="var(--ornament)" stroke-width="4"/>

      <circle cx="111" cy="506" r="35" fill="var(--yellow)"/>
      <path d="M111 484 L117 500 L134 500 L120 510 L125 527 L111 517 L97 527 L102 510 L88 500 L105 500 Z" fill="var(--ink)"/>

      <g class="icon icon--person">
        <circle cx="497" cy="273" r="36" fill="var(--lime)"/>
        <circle cx="497" cy="263" r="11" fill="var(--ink)"/>
        <path d="M477 296 C479 281 515 281 517 296 Z" fill="var(--ink)"/>
      </g>
      <g class="icon icon--phone">
        <circle cx="497" cy="368" r="36" fill="var(--red)"/>
        <rect x="485" y="345" width="24" height="46" rx="4" fill="var(--ink)"/>
        <rect x="488" y="351" width="18" height="32" fill="#ffffff"/>
        <circle cx="497" cy="387" r="2" fill="#ffffff"/>
      </g>
      <g class="icon icon--mail">
        <circle cx="497" cy="458" r="36" fill="var(--violet)"/>
        <rect x="478" y="447" width="38" height="26" fill="none" stroke="var(--ink)" stroke-width="3"/>
        <path d="M478 447 L497 462 L516 447 M478 473 L492 459 M516 473 L502 459" fill="none" stroke="var(--ink)" stroke-width="3"/>
      </g>
    </svg>

    <h1 class="brand-title">KITE &amp; LANTERN</h1>
    <p class="tagline">- personalizing education -</p>
    <p class="logo-mark__name">Kite &amp; Lantern</p>
    <p class="contact-line contact-line--name">Maren Tolliver | Co-founder</p>
    <p class="contact-line contact-line--phone">90412736</p>
    <p class="contact-line contact-line--email">kitenlantern@mailbox.com</p>
  </section>

  <section class="card card--back">
    <svg class="card__shapes" width="1032" height="596" viewBox="0 0 1032 596">
      <path d="M152 0 H441 C446 40 420 76 360 82 C290 88 200 86 166 64 C150 50 148 20 152 0 Z" fill="var(--rose)"/>
      <path d="M770 0 H1032 V156 C980 162 860 150 790 120 C752 90 756 30 770 0 Z" fill="var(--yellow)"/>
      <rect x="507" y="415" width="50" height="42" rx="10" fill="var(--olive)"/>
      <path d="M640 460 C670 452 706 456 712 480 C718 520 712 550 690 554 C660 558 632 552 628 530 C622 500 626 466 640 460 Z" fill="var(--crimson)"/>
      <path d="M0 534 C40 528 110 530 126 560 L130 596 H0 Z" fill="var(--lime)"/>
      <path d="M40 30 C120 40 150 140 130 240 C110 340 150 420 230 470 C270 500 300 540 290 560 L40 560 Z"
            fill="var(--ornament)" opacity="0.12" role="img" aria-label="Decorative swirling flourish ornament"/>
    </svg>

    <h2 class="brand-title">KITE &amp; LANTERN</h2>
    <p class="quote">"The key to this transformation is not to standardize<br>
      education, but to personalize it, to build achievement<br>
      on discovering the individual talents of each child, to<br>
      put students in n evironment where they want to<br>
      learn and where they can naturally discover they<br>
      true passions."</p>
    <p class="quote__author">- Alden Marsh -</p>
  </section>

</main>
</body>
</html>
```